Meal Prep website

Website needed for local meal prep service. Simple template to start off with and then looking to be able to take orders from members

Target Market(s)

Toronto area fitness professionals, athletes and people looking for become healthier

Industry/Entity Type

It Service

Number of Pages Required

5+ page

Font styles to use
Sans Serif

Colors
000000

Requirements
Must have
• Landing page giving information about who we are and what type of service we provide.
• Links to social media. Dishvaultfood on Instagram
Nice to have
• E-commerce section allowing users to select and place orders while accepting payments

```html
<!DOCTYPE html>
<html lang="en">
<head>
<meta charset="utf-8">
<title>Dishvault – Meal Prep Service</title>
<link href="https://fonts.googleapis.com/css2?family=Raleway:wght@600;700;800&family=Open+Sans:wght@400;600;700&display=swap" rel="stylesheet">
<style>
:root{
  --dark:#2a2a2a;
  --darker:#1e1e1e;
  --forest:#3f6b3b;
  --forest-deep:#345b31;
  --lime:#7db23f;
  --lime-bright:#8cc63f;
  --lime-btn:#6fa12f;
  --white:#ffffff;
  --muted:#cfd6cb;
  --text:#5a5a5a;
  --star:#f2b01e;
}
*{box-sizing:border-box;margin:0;padding:0}
html,body{width:1200px;height:3400px;overflow:hidden}
body{font-family:"Open Sans",Arial,sans-serif;color:var(--white);background:var(--dark);position:relative}
h1,h2,h3,.brand,.nav a,.btn{font-family:"Raleway","Open Sans",sans-serif}
section,header,footer{position:absolute;left:0;width:1200px}

/* header */
.site-header{top:0;height:104px;z-index:3}
.topbar{height:58px;background:rgba(20,20,20,.82);display:flex;align-items:center;padding:0 70px}
.brand{font-size:34px;font-weight:800;color:var(--white);display:flex;align-items:center;gap:10px}
.brand-dot{width:16px;height:16px;border-radius:50%;background:var(--lime-bright)}
.top-links{margin-left:auto;display:flex;align-items:center;gap:34px;font-size:13px;font-weight:600;letter-spacing:.5px}
.top-links .phone{display:flex;align-items:center;gap:8px;color:var(--lime-bright);margin-right:50px}
.nav{height:46px;background:rgba(30,30,30,.7);display:flex;align-items:center;padding:0 70px;gap:38px}
.nav a{color:var(--white);text-decoration:none;font-size:15px;font-weight:700}
.nav a.active{color:var(--lime-bright)}
.search{margin-left:auto;display:flex;align-items:center;gap:10px;width:200px;border-bottom:1px solid #777;font-size:13px;color:#bbb;padding-bottom:3px}
.search span{flex:1}

/* hero */
.hero{top:0;height:640px}
.hero-photo{position:absolute;inset:0;background:linear-gradient(120deg,#3a2c20 0%,#6b4a2a 25%,#4d5a2d 50%,#7a3b22 75%,#2f2a24 100%)}
.hero-shade{position:absolute;inset:0;background:rgba(0,0,0,.35)}
.hero-copy{position:absolute;top:268px;width:100%;text-align:center}
.hero-copy h1{font-size:76px;font-weight:800;color:var(--lime-bright);letter-spacing:3px;line-height:1}
.hero-copy p{font-family:"Raleway",sans-serif;font-size:46px;font-weight:700;margin-top:14px}
.dots{position:absolute;top:598px;width:100%;display:flex;justify-content:center;gap:10px}
.dots i{width:10px;height:10px;border-radius:50%;background:rgba(255,255,255,.5)}
.dots i.on{background:var(--white)}

/* welcome */
.welcome{top:640px;height:340px;background:var(--dark)}
.welcome-card{position:absolute;left:72px;top:58px;width:1056px;height:230px;background:var(--white);display:flex;align-items:center;padding:0 40px}
.welcome-title{width:270px;color:var(--dark)}
.welcome-title h2{font-size:30px;font-weight:800;line-height:1.1}
.welcome-title .brand{color:var(--forest);font-size:38px;margin-top:4px}
.welcome-body{flex:1;border-left:2px solid #e3e3e3;padding-left:34px;color:var(--text);font-size:14px;line-height:1.6}

/* split blocks */
.who{top:980px;height:360px}
.about{top:1340px;height:380px}
.photo{position:absolute;top:0;height:100%;width:600px}
.panel{position:absolute;top:0;height:100%;width:600px;padding:44px 60px}
.panel h2{font-size:38px;font-weight:800;margin-bottom:16px}
.panel p{font-size:14px;line-height:1.65;color:var(--muted)}
.btn{display:inline-block;font-size:13px;font-weight:700;letter-spacing:.5px;border-radius:20px;padding:8px 26px}
.btn-outline{border:2px solid var(--white);color:var(--white);margin-top:22px}
.btn-solid{background:linear-gradient(#8fc94a,var(--lime-btn));color:var(--white)}

/* order */
.order{top:1720px;height:540px;background:var(--lime)}
.order h2{text-align:center;font-size:40px;font-weight:800;margin-top:42px}
.cards{position:absolute;top:112px;left:72px;display:flex;gap:26px}
.card{width:250px;height:380px;background:var(--white);border-radius:12px;overflow:hidden;text-align:center;color:var(--dark)}
.card-photo{height:210px}
.stars{color:var(--star);font-size:15px;letter-spacing:2px;margin-top:14px}
.card h3{font-size:16px;font-weight:800;margin-top:4px}
.card .desc{font-size:13px;color:#777;margin-top:4px}
.card .price{font-size:26px;font-weight:700;margin-top:6px}
.card .price small{font-size:12px;color:#888}
.card .btn{margin-top:8px;padding:6px 30px}

/* blog + reviews */
.stories{top:2260px;height:460px;background:var(--dark)}
.stories h2{font-size:38px;font-weight:800}
.blog{position:absolute;left:72px;top:50px;width:660px}
.post{display:flex;gap:26px;margin-top:30px}
.post-photo{width:180px;height:128px;flex:none;border-radius:4px}
.post h3{font-size:16px;font-weight:700;color:var(--lime-bright);text-transform:uppercase}
.post p{font-size:13px;line-height:1.6;color:var(--muted);margin-top:6px}
.post .more{font-size:12px;color:var(--lime-bright);margin-top:6px}
.reviews{position:absolute;left:780px;top:50px;width:348px}
.quote{background:var(--white);color:var(--text);border-radius:10px;padding:26px 26px;margin-top:30px;font-size:13px;line-height:1.65;font-style:italic;position:relative}
.quote::after{content:"";position:absolute;left:40px;bottom:-16px;border:16px solid transparent;border-bottom:0;border-top-color:var(--white)}
.reviewer{margin:30px 0 0 40px;font-size:12px}
.reviewer b{display:block;font-weight:700}
.reviewer span{color:#aaa}
.arrows{position:absolute;right:0;bottom:-30px;display:flex;gap:12px;color:var(--lime-bright)}

/* newsletter */
.newsletter{top:2720px;height:220px;background:var(--lime);text-align:center}
.newsletter h2{font-size:38px;font-weight:800;margin-top:36px}
.newsletter p{font-size:14px;margin-top:10px}
.signup{width:540px;height:46px;margin:22px auto 0;background:var(--white);border-radius:24px;display:flex;align-items:center;padding:0 4px 0 24px;color:#999;font-size:13px}
.signup span{flex:1;text-align:left}
.signup .btn{padding:9px 32px}

/* footer */
.site-footer{top:2940px;height:460px;background:var(--darker)}
.footer-brand{text-align:center;margin-top:44px;justify-content:center}
.footer-cols{position:absolute;top:118px;left:72px;width:1056px;display:flex;gap:56px}
.footer-cols h3{font-size:15px;font-weight:800;margin-bottom:14px;text-transform:uppercase}
.links{display:grid;grid-template-columns:110px 110px;font-size:13px;line-height:2;color:#bbb}
.gallery{display:grid;grid-template-columns:repeat(3,78px);gap:8px}
.gallery div{height:64px}
.contact li{list-style:none;font-size:13px;color:#bbb;line-height:2;display:flex;align-items:center;gap:8px}
.map{width:220px;height:180px;margin-top:30px;background:linear-gradient(135deg,#d9dcd4,#c6ccbf)}
.bottom{position:absolute;bottom:0;left:0;width:1200px;height:60px;border-top:1px solid #333;display:flex;align-items:center;padding:0 72px;font-size:12px;color:#888}
.follow{margin-left:auto;display:flex;align-items:center;gap:12px;color:var(--white);font-size:14px}
.follow i{width:26px;height:26px;border-radius:50%;background:#555}
</style>
</head>
<body>

<header class="site-header">
  <div class="topbar">
    <div class="brand"><span class="brand-dot"></span>Dishvault</div>
    <div class="top-links">
      <span class="phone">
        <svg width="14" height="14" viewBox="0 0 24 24"><path fill="#8cc63f" d="M6.6 10.8a15 15 0 0 0 6.6 6.6l2.2-2.2a1 1 0 0 1 1-.25 11.4 11.4 0 0 0 3.6.57 1 1 0 0 1 1 1V20a1 1 0 0 1-1 1A17 17 0 0 1 3 4a1 1 0 0 1 1-1h3.5a1 1 0 0 1 1 1c0 1.25.2 2.45.57 3.57a1 1 0 0 1-.25 1z"/></svg>
        1-800-555-0192
      </span>
      <span>LOGIN</span><span>REGISTER</span>
    </div>
  </div>
  <nav class="nav">
    <a class="active">Home</a><a>About Us</a><a>Services</a><a>Menu</a><a>Blog</a><a>Gallery</a><a>Reviews</a><a>Contact Us</a>
    <div class="search"><span>Search</span>
      <svg width="14" height="14" viewBox="0 0 24 24"><circle cx="10" cy="10" r="7" stroke="#fff" stroke-width="2.5" fill="none"/><path d="M15 15l6 6" stroke="#fff" stroke-width="2.5"/></svg>
    </div>
  </nav>
</header>

<section class="hero">
  <div class="hero-photo" role="img" aria-label="Rows of meal prep containers filled with fresh prepared dishes"></div>
  <div class="hero-shade"></div>
  <div class="hero-copy">
    <h1>DISHVAULT</h1>
    <p>We provide meal prep service</p>
  </div>
  <div class="dots"><i class="on"></i><i></i><i></i><i></i></div>
</section>

<section class="welcome">
  <div class="welcome-card">
    <div class="welcome-title">
      <h2>WELCOME TO</h2>
      <div class="brand">Dishvault</div>
    </div>
    <div class="welcome-body">
      <p>Fresh, balanced meals cooked every week in our local kitchen and delivered across the city. We plan portions around your goals, whether you train daily, compete in sport or simply want to eat better without the hassle of shopping and cooking. Pick your plan, choose your dishes and let us handle the rest so you can focus on training, work and family.</p>
      <span class="btn btn-solid" style="margin-top:16px">READ MORE</span>
    </div>
  </div>
</section>

<section class="who">
  <div class="photo" style="left:0;background:linear-gradient(135deg,#c9c2b4,#8e7a5e 60%,#5d6b3c)" role="img" aria-label="Hands packing fresh meals into prep containers"></div>
  <div class="panel" style="left:600px;background:var(--forest)">
    <h2>WHO WE ARE</h2>
    <p>We are a small team of cooks and nutrition coaches who believe healthy food should be simple. Every meal is made from fresh local ingredients, measured for protein, carbs and fats, and packed the same day. Our clients include trainers, athletes and busy people who want real food that fuels them well.</p>
    <span class="btn btn-outline">READ MORE</span>
  </div>
</section>

<section class="about">
  <div class="panel" style="left:0;background:var(--forest-deep)">
    <h2>ABOUT OUR SERVICES</h2>
    <p>Choose from weekly plans, single meal orders or custom menus built around your macros. We offer lean protein bowls, vegetarian options and low carb dishes, all ready to heat and eat. Orders placed by Thursday are delivered fresh on Sunday, with pickup also available at our kitchen.</p>
    <span class="btn btn-outline">READ MORE</span>
  </div>
  <div class="photo" style="left:600px;background:linear-gradient(135deg,#b9b9b4,#7f8a5a 50%,#a45a35)" role="img" aria-label="Foil trays of roasted chicken, vegetables and rice"></div>
</section>

<section class="order">
  <h2>PLACE YOUR ORDER</h2>
  <div class="cards">
    <div class="card">
      <div class="card-photo" style="background:linear-gradient(135deg,#6a2a1a,#c8501f)" role="img" aria-label="Trays of tomato based meals"></div>
      <div class="stars">★★★★★</div><h3>PRODUCT TITLE</h3><p class="desc">Duis aliquam nibh a dui</p>
      <p class="price">$5.00 <small>p.w</small></p><span class="btn btn-solid">ORDER NOW</span>
    </div>
    <div class="card">
      <div class="card-photo" style="background:linear-gradient(135deg,#4f8a2a,#d9a92a)" role="img" aria-label="Fresh vegetable salad in containers"></div>
      <div class="stars">★★★★★</div><h3>PRODUCT TITLE</h3><p class="desc">Duis aliquam nibh a dui</p>
      <p class="price">$5.00 <small>p.w</small></p><span class="btn btn-solid">ORDER NOW</span>
    </div>
    <div class="card">
      <div class="card-photo" style="background:linear-gradient(135deg,#2c2c2c,#7a5a3a)" role="img" aria-label="Black meal boxes with grilled meat and greens"></div>
      <div class="stars">★★★★★</div><h3>PRODUCT TITLE</h3><p class="desc">Duis aliquam nibh a dui</p>
      <p class="price">$5.00 <small>p.w</small></p><span class="btn btn-solid">ORDER NOW</span>
    </div>
    <div class="card">
      <div class="card-photo" style="background:linear-gradient(135deg,#b99a72,#8a6040)" role="img" aria-label="Baked meatballs on a tray"></div>
      <div class="stars">★★★★★</div><h3>PRODUCT TITLE</h3><p class="desc">Duis aliquam nibh a dui</p>
      <p class="price">$5.00 <small>p.w</small></p><span class="btn btn-solid">ORDER NOW</span>
    </div>
  </div>
</section>

<section class="stories">
  <div class="blog">
    <h2>BLOG POSTS</h2>
    <div class="post">
      <div class="post-photo" style="background:linear-gradient(135deg,#d6c9a8,#9a8a5a)" role="img" aria-label="Packed lunch box on a table"></div>
      <div>
        <h3>Aliquam molestie, mi at imperdiet euismod</h3>
        <p>Simple tips for planning a week of balanced meals, from prepping grains in bulk to storing cooked protein safely so every lunch stays fresh and tasty.</p>
        <p class="more">Continue Reading</p>
      </div>
    </div>
    <div class="post">
      <div class="post-photo" style="background:linear-gradient(135deg,#3d6a2a,#c0492a)" role="img" aria-label="Colourful vegetable dishes"></div>
      <div>
        <h3>Aliquam molestie, mi at imperdiet euismod</h3>
        <p>How athletes can time their meals around training sessions, and which of our dishes work best before a workout and during recovery afterwards.</p>
        <p class="more">Continue Reading</p>
      </div>
    </div>
  </div>
  <div class="reviews">
    <h2>REVIEWS</h2>
    <div class="quote">“ The meals are fresh, filling and perfectly portioned. I save hours every week and my training has never felt better. Delivery is always on time and the menu keeps changing. ”</div>
    <div class="reviewer"><b>MARK JENSEN</b><span>Toronto</span></div>
    <div class="arrows">
      <svg width="12" height="16" viewBox="0 0 12 16"><path d="M9 2L3 8l6 6" stroke="#8cc63f" stroke-width="2.5" fill="none"/></svg>
      <svg width="12" height="16" viewBox="0 0 12 16"><path d="M3 2l6 6-6 6" stroke="#8cc63f" stroke-width="2.5" fill="none"/></svg>
    </div>
  </div>
</section>

<section class="newsletter">
  <h2>NEWSLETTER SIGN UP</h2>
  <p>Get new menus, seasonal dishes and member offers sent to your inbox every week, free of charge and easy to cancel.</p>
  <div class="signup"><span>Enter Email Address</span><span class="btn btn-solid">SIGN UP</span></div>
</section>

<footer class="site-footer">
  <div class="brand footer-brand"><span class="brand-dot"></span>Dishvault</div>
  <div class="footer-cols">
    <div>
      <h3>Site Map</h3>
      <div class="links"><span>Home</span><span>Gallery</span><span>About Us</span><span>Reviews</span><span>Services</span><span>Contact Us</span><span>Menu</span><span></span><span>Blog</span></div>
    </div>
    <div>
      <h3>Gallery</h3>
      <div class="gallery" role="img" aria-label="Thumbnails of prepared meals">
        <div style="background:#8a4a22"></div><div style="background:#c7a23a"></div><div style="background:#4d7a2a"></div>
        <div style="background:#5a3a2a"></div><div style="background:#a8643a"></div><div style="background:#3f6b3b"></div>
      </div>
    </div>
    <div>
      <h3>Contact Info</h3>
      <ul class="contact">
        <li>12 Orchard Lane</li>
        <li>Toronto, ON M5V 2T6</li>
        <li><svg width="12" height="12" viewBox="0 0 24 24"><path fill="#8cc63f" d="M6.6 10.8a15 15 0 0 0 6.6 6.6l2.2-2.2a1 1 0 0 1 1-.25 11.4 11.4 0 0 0 3.6.57 1 1 0 0 1 1 1V20a1 1 0 0 1-1 1A17 17 0 0 1 3 4a1 1 0 0 1 1-1h3.5a1 1 0 0 1 1 1c0 1.25.2 2.45.57 3.57a1 1 0 0 1-.25 1z"/></svg>1-800-555-0192</li>
        <li><svg width="12" height="12" viewBox="0 0 24 24"><rect x="2" y="5" width="20" height="14" fill="none" stroke="#8cc63f" stroke-width="2"/><path d="M2 5l10 8 10-8" fill="none" stroke="#8cc63f" stroke-width="2"/></svg>hello@dishvaultfood.com</li>
        <li><svg width="12" height="12" viewBox="0 0 24 24"><path fill="#8cc63f" d="M12 2a7 7 0 0 0-7 7c0 5 7 13 7 13s7-8 7-13a7 7 0 0 0-7-7zm0 9.5A2.5 2.5 0 1 1 12 6.5a2.5 2.5 0 0 1 0 5z"/></svg>Locate Map</li>
      </ul>
    </div>
    <div class="map" role="img" aria-label="Street map showing the kitchen location"></div>
  </div>
  <div class="bottom">
    <span>Copyright © 2024 Dishvault. All rights reserved.</span>
    <div class="follow">Follow Us <i></i></div>
  </div>
</footer>

</body>
</html>
```